30 Nights of Light Flyer Leading up to Easter

We want to push a campaign in March called 30 Nights of Light. Its to send light to you and shine light through you. It will be daily emails and text messages of encouragement and challenges that will either encourage you or help you encourage someone else. I want to create a graphic that invites people to be a part of this 30 night challenge. This will be sponsored by our church. Ultimately, I will create an event on Facebook, Instagram and Tik Tok asking people to sign up to be a part of this 30 Nights of Light campaign.

I need a graphic with the words:
30 Nights of Light
To Send Light to You and Shine Light Through You
Beginning March 9th, leading up to Resurrection Weekend (Easter)
Harbor Church (Logo) Included

Our church colors are red and blue. You will be able to pull those colors from the logo we upload. I will also upload some pics you can use but you don't have to use them. If there is better stock photos you have that would get the point across, please feel free. I would love this in 16x9 (1920x1080 px). I do have the AI or EPS fil for the logo if needed.
Updates

Another designer asked me to extend the deadline so they can submit. Will be choosing a design today. Martin Hale

Target Market(s)

Thos who are hopeless and those who want to spread hope to others.

Industry/Entity Type

Church

Requirements
Must have
• These are in the description
Nice to have
• You don't have to use the pictures I sent. Stock photos are just fine. Would like a simple design as it is an invitation for people to join us in 30 nights of light.

```html
<!DOCTYPE html>
<html lang="en">
<head>
<meta charset="utf-8">
<title>30 Nights of Light – Harbor Church</title>
<link rel="stylesheet" href="https://fonts.googleapis.com/css2?family=Montserrat:wght@800;900&family=Oswald:wght@400&display=swap">
<style>
  :root {
    --brand-red: #cc2022;
    --brand-navy: #0c0c6e;
    --band-navy: #13137a;
    --sky-light: #fbe7a8;
    --sky-warm: #f0b45a;
    --field-amber: #b8742e;
    --white: #ffffff;
  }
  html, body {
    margin: 0;
    padding: 0;
    width: 1200px;
    height: 675px;
    overflow: hidden;
    background: #ffffff;
  }
  .flyer {
    position: relative;
    width: 1200px;
    height: 675px;
    overflow: hidden;
    font-family: "Montserrat", sans-serif;
  }
  .scene-photo {
    position: absolute;
    inset: 0;
    background:
      radial-gradient(ellipse 30% 40% at 4% 68%, rgba(255,255,240,0.95), rgba(255,240,200,0) 70%),
      radial-gradient(ellipse 55% 45% at 55% 18%, rgba(255,245,205,0.9), rgba(255,230,170,0) 70%),
      linear-gradient(180deg, var(--sky-light) 0%, var(--sky-warm) 45%, #d89a4a 70%, var(--field-amber) 100%);
  }
  .scene-photo::after {
    content: "";
    position: absolute;
    right: 0;
    top: 35%;
    width: 32%;
    height: 55%;
    background: radial-gradient(ellipse at 60% 60%, rgba(120,110,50,0.45), rgba(120,110,50,0) 70%);
  }
  .headline {
    position: absolute;
    inset: 0;
  }
  .headline .number { fill: var(--brand-red); font-weight: 900; }
  .headline .nights { fill: var(--brand-red); font-weight: 900; }
  .headline .of-light { fill: var(--brand-navy); font-weight: 900; }

  .brand {
    position: absolute;
    right: 38px;
    top: 86px;
    display: flex;
    align-items: center;
    gap: 8px;
  }
  .brand-mark {
    width: 16px;
    height: 16px;
    background: var(--brand-red);
  }
  .brand-name {
    font-family: "Montserrat", sans-serif;
    font-weight: 800;
    font-size: 26px;
    letter-spacing: 0.5px;
    color: var(--brand-navy);
    text-transform: uppercase;
  }
  .rule {
    position: absolute;
    left: 0;
    top: 552px;
    width: 1200px;
    height: 12px;
    background: var(--brand-red);
  }
  .message-band {
    position: absolute;
    left: 0;
    top: 564px;
    width: 1200px;
    height: 111px;
    background: linear-gradient(180deg, #1a1a88 0%, var(--band-navy) 100%);
  }
  .message {
    position: absolute;
    left: 150px;
    top: 576px;
    margin: 0;
    width: 960px;
    font-family: "Oswald", sans-serif;
    font-weight: 400;
    font-size: 33px;
    line-height: 43px;
    color: var(--white);
    text-transform: uppercase;
    letter-spacing: 0;
  }
</style>
</head>
<body>
  <main class="flyer">
    <div class="scene-photo" role="img" aria-label="Golden sunrise over a meadow with a small white country church, trees and a softly glowing light on the left"></div>

    <svg class="headline" width="1200" height="675" viewBox="0 0 1200 675" aria-label="30 Nights of Light">
      <text class="number" x="150" y="372" font-size="410" textLength="381" lengthAdjust="spacingAndGlyphs">30</text>
      <text class="nights" transform="translate(554 84) rotate(90)" font-size="112" textLength="286" lengthAdjust="spacingAndGlyphs">NIGHTS</text>
      <text class="of-light" x="140" y="462" font-size="110" textLength="488" lengthAdjust="spacingAndGlyphs">OF LIGHT</text>
    </svg>

    <div class="brand">
      <span class="brand-mark"></span>
      <span class="brand-name">Harbor Church</span>
    </div>

    <div class="rule"></div>
    <div class="message-band"></div>
    <p class="message">To send light to you and shine light through you beginning March 9th, leading up to Resurrection Weekend (Easter)</p>
  </main>
</body>
</html>
```